Tarvell homes and renovations business card design.

Would like some new card designs utilizing my new logo that look professional. I am open to different colors on the logo or utilize the same ones we have. I like the original concept but would like to see some fresh ideas and build on what we have already done.

Target Market(s)

Custom home building industry, Real estate sales, Renovation projects.

Industry/Entity Type

Home Builder

Contact Information for Business Card

Tarvell Homes and Renovations
2871 162nd Street
Brenholt, Norland
T0L3P0
Home : 403- 555-0187 Cell: 403- 555-0243

My info is : Gus Tarvell, President and CEO
email: tarvellhomes@quillmail.example
Website: tarvellhomes.example

Requirements
Must have
• Must Use my new logo design. I am open to different colors on the logo or utilize the same ones in the existing design. I can upload the original logo design if needed.

```html
<!DOCTYPE html>
<html lang="en">
<head>
<meta charset="utf-8">
<title>Tarvell Homes and Renovations – Business Card</title>
<link rel="stylesheet" href="https://fonts.googleapis.com/css2?family=Open+Sans:wght@400;600;700&display=swap">
<style>
  :root {
    --page: #e9e6e1;
    --card-white: #ffffff;
    --card-black: #262626;
    --gold: #b8862e;
    --gold-text: #b07f2a;
    --yellow: #f8b91c;
    --ink: #1e1e1e;
    --name-light: #f2f2f2;
  }
  * { box-sizing: border-box; margin: 0; padding: 0; }
  html, body {
    width: 1200px; height: 900px; overflow: hidden;
    background: var(--page);
    font-family: "Open Sans", Arial, sans-serif;
  }
  .canvas {
    width: 1200px; height: 900px;
    display: flex; flex-direction: column; align-items: center; justify-content: center;
    gap: 40px;
  }
  .card {
    position: relative;
    width: 680px; height: 388px;
    box-shadow: 0 6px 18px rgba(0,0,0,.18);
    overflow: hidden;
  }
  .card--back { background: var(--card-black); display: flex; align-items: center; justify-content: center; }
  .card--front { background: var(--card-white); }

  .brand-name { font-weight: 600; line-height: 1.2; text-align: center; }
  .card--back .brand-name { color: var(--name-light); font-size: 38px; }
  .card--front .brand-name {
    position: absolute; left: 390px; top: 152px; width: 260px;
    color: var(--gold); font-size: 26px;
  }

  .card__bands { position: absolute; inset: 0; }

  .person { position: absolute; left: 74px; top: 26px; }
  .person__name { color: var(--gold-text); font-weight: 700; font-size: 19px; }
  .person__title { color: var(--ink); font-size: 12.5px; margin-top: 1px; }

  .contact-list { position: absolute; left: 30px; top: 96px; list-style: none; }
  .contact-list li { display: flex; align-items: center; gap: 8px; font-size: 15px; color: var(--ink); line-height: 20px; }
  .contact-list svg { width: 11px; height: 11px; flex: none; fill: var(--gold); }

  .address { position: absolute; left: 30px; top: 196px; font-size: 14.5px; color: var(--ink); line-height: 19px; font-style: normal; }
  .address__company { color: var(--gold-text); font-weight: 700; font-size: 15.5px; }
</style>
</head>
<body>
<main class="canvas">

  <section class="card card--back" aria-label="Card back">
    <p class="brand-name">Tarvell Homes and Renovations</p>
  </section>

  <section class="card card--front" aria-label="Card front">
    <svg class="card__bands" viewBox="0 0 680 388" aria-hidden="true">
      <polygon points="0,22 34,22 26,52 0,52" fill="var(--gold)"/>
      <polygon points="38,22 58,22 50,52 30,52" fill="var(--yellow)"/>
      <polygon points="0,262 300,262 292,286 0,286" fill="var(--gold)"/>
      <polygon points="300,292 680,292 680,368 276,368" fill="var(--yellow)"/>
    </svg>

    <div class="person">
      <p class="person__name">Gus Tarvell</p>
      <p class="person__title">President and CEO</p>
    </div>

    <ul class="contact-list">
      <li>
        <svg viewBox="0 0 24 24"><path d="M6.6 10.8a15.2 15.2 0 0 0 6.6 6.6l2.2-2.2a1 1 0 0 1 1-.25 11.4 11.4 0 0 0 3.6.57 1 1 0 0 1 1 1V20a1 1 0 0 1-1 1A17 17 0 0 1 3 4a1 1 0 0 1 1-1h3.5a1 1 0 0 1 1 1c0 1.25.2 2.45.57 3.57a1 1 0 0 1-.25 1z"/></svg>
        403- 555-0187
      </li>
      <li>
        <svg viewBox="0 0 24 24"><path d="M7 1h10a2 2 0 0 1 2 2v18a2 2 0 0 1-2 2H7a2 2 0 0 1-2-2V3a2 2 0 0 1 2-2zm0 3v14h10V4z"/></svg>
        403- 555-0243
      </li>
      <li>
        <svg viewBox="0 0 24 24"><path d="M2 4h20v16H2zm2 2v.5l8 5 8-5V6zm0 3v9h16V9l-8 5z"/></svg>
        tarvellhomes@quillmail.example
      </li>
      <li>
        <svg viewBox="0 0 24 24"><circle cx="12" cy="12" r="11"/></svg>
        tarvellhomes.example
      </li>
    </ul>

    <address class="address">
      <span class="address__company">Tarvell homes and Renovations</span><br>
      2871 162nd Street Brenholt, Norland<br>
      T0L3P0
    </address>

    <p class="brand-name">Tarvell Homes and Renovations</p>
  </section>

</main>
</body>
</html>
```